Real Estate Agent Service Brochure

I need a trifold brochure to showcase my real estate services. I am a veteran Real Estate Broker specializing in marketing properties for sale and for top dollar. I would like to see designs that use colors from my logo (attached) and I would like to showcase some before and after photos of staging jobs I have done to homes to get them ready for the market. This brochure is specific to home sellers. You are happy to go check out my website for inspiration www.lomavertpa.com but keep the copy as I have written it. The the final design should communicate experienced professional who uses current technologies and strategies to market properties for the highest value.

Target Market(s)

Homeowners wanting to sell their homes

Industry/Entity Type

Real Estate Agent

Font styles to use
Serif

Requirements
Must have
• My, logo, personal photo, title and contact information as listed:
• Marta Venholt
• Owner Broker
• Stager Re-Designer
• 860-912-7048
• BRAVE Realty LLC
• LOMAVERTPA.com
• Marta@LOMAVERTPA.com
• The colors used should be those in my logo.
• Brochure should be able to fit in standard envelope for mailing.
Nice to have
• I think I would like my personal photo and contact information on the front panel.
Should not have
• Bright colors.

```html
<!DOCTYPE html>
<html lang="en">
<head>
<meta charset="utf-8">
<title>BRAVE Realty LLC – Seller Brochure</title>
<link href="https://fonts.googleapis.com/css2?family=Source+Sans+3:ital,wght@0,400;0,600;0,700;1,600&display=swap" rel="stylesheet">
<style>
:root{
  --navy:#1f2d5c;
  --slate:#58585a;
  --ink:#3a3a3c;
  --page:#ffffff;
  --paper-shade:#ececec;
  --backdrop:#eeeeef;
  --thumb-bg:#f3f3f3;
}
*{box-sizing:border-box;margin:0;padding:0}
html,body{width:804px;height:1200px;overflow:hidden}
body{background:var(--backdrop);font-family:"Source Sans 3",Arial,sans-serif;color:var(--ink);position:relative}
.spread{position:absolute;left:27px;width:800px;height:620px;transform:scale(.9375);transform-origin:0 0;background:var(--page);overflow:hidden}
.spread--outside{top:10px}
.spread--inside{top:609px}
.abs{position:absolute}
.photo{position:absolute}
.fold{position:absolute;top:0;width:14px;height:620px;pointer-events:none}
.fold--a{background:linear-gradient(90deg,rgba(0,0,0,.10),rgba(0,0,0,0))}
.fold--b{background:linear-gradient(270deg,rgba(0,0,0,.08),rgba(0,0,0,0))}

/* outside */
.band-top{left:0;top:0;width:800px;height:105px;background:var(--slate)}
.band-bottom{height:22px;background:var(--slate);top:598px}
.clients-heading{left:14px;top:36px;width:240px;color:#fff;font-size:16px;line-height:21px}
.site-top{left:262px;top:52px;width:263px;text-align:center;color:#fff;font-size:11px;letter-spacing:.3px}
.brand{font-weight:600;text-align:center;line-height:1}
.brand__name{font-size:40px;letter-spacing:2px}
.brand__sub{font-size:9px;letter-spacing:6px;margin-top:5px}
.brand--light{color:#fff}
.brand--navy{color:var(--navy)}
.testimonials{left:0;top:105px;width:262px;height:493px;background:linear-gradient(90deg,#fff 60%,#e6e6e6);padding:8px 18px 0 14px}
.quote{font-size:7px;line-height:9.6px;text-align:justify;margin-bottom:8px}
.quote::before{content:"\201C";color:#a8a8a8;font-size:15px;font-weight:700;line-height:0;vertical-align:-4px;margin-right:3px}
.quote__by{display:block;text-align:left}
.headline-box{left:543px;top:404px;width:257px;height:86px;background:var(--navy);color:#fff;text-align:right;padding:10px 26px 0 0;font-size:21px;line-height:32px;letter-spacing:1px}
.contact-panel{left:262px;top:404px;width:281px;height:194px;background:linear-gradient(180deg,#fff,var(--paper-shade))}
.contact-panel .brand{position:absolute;left:0;width:263px;top:42px}
.contact-list{position:absolute;left:63px;top:137px;list-style:none;color:var(--navy);font-size:11px;font-weight:600}
.contact-list li{height:18px;display:flex;align-items:center;gap:6px}
.icon{width:11px;height:11px;flex:none}
.agent{left:543px;top:490px;width:257px;height:108px;background:linear-gradient(180deg,#fff,#f1f1f1);text-align:right;padding:8px 26px 0 0;color:var(--navy)}
.agent__name{font-size:16px;line-height:18px}
.agent__role{font-size:10px;line-height:11px}
.agent__contacts{list-style:none;margin-top:13px;font-size:9px;font-weight:600}
.agent__contacts li{height:14px;display:flex;justify-content:flex-end;align-items:center;gap:5px}

/* inside */
.intro{left:0;top:0;width:265px;height:620px;background:var(--page)}
.intro .brand{position:absolute;left:0;width:265px;top:22px}
.intro__text{position:absolute;left:16px;top:112px;width:236px;font-size:10.6px;line-height:13px;text-align:justify}
.intro__text p{margin-bottom:13px}
.staging{left:265px;top:135px;width:535px;height:183px;background:var(--thumb-bg)}
.thumb{position:absolute;width:116px;height:80px;border:3px solid #fff;box-shadow:0 1px 3px rgba(0,0,0,.3)}
.thumb__label{position:absolute;left:4px;bottom:2px;color:#fff;font-size:7px;font-weight:600;font-style:italic;letter-spacing:.3px}
.copy{top:335px;font-size:10.2px;line-height:13px;text-align:justify}
.copy p{margin-bottom:13px}
.copy h3{color:var(--navy);font-size:10.5px;font-weight:700;margin-bottom:13px}
.site-button{left:595px;top:557px;width:205px;height:30px;background:var(--navy);color:#fff;font-size:11px;letter-spacing:.4px;display:flex;align-items:center;justify-content:center}
</style>
</head>
<body>

<section class="spread spread--outside">
  <div class="abs band-top"></div>
  <p class="abs clients-heading">This is what Marta’s clients say about their experiences:</p>
  <p class="abs site-top">www.lomavertpa.com</p>
  <div class="abs brand brand--light" style="left:543px;top:22px;width:257px">
    <div class="brand__name">BRAVE</div>
    <div class="brand__sub">REALTY LLC</div>
  </div>

  <div class="abs testimonials">
    <p class="quote">Marta guided us from day one, preparing a market evaluation with current data to set a fair list price. She staged our home, arranged great photography and video tours, and received several offers in the first weekend. We were truly impressed by her knowledge and work ethic.<span class="quote__by">Paul &amp; Ana R.</span></p>
    <p class="quote">Marta and her team are knowledgeable and professional. I have worked with her on three separate transactions and am always pleased with her negotiating skills, her market knowledge and her ability to manage the process.<span class="quote__by">Lydia T.</span></p>
    <p class="quote">So glad we found Marta to help stage a property we had just finished renovating. She listened to our ideas, arranged the spaces to suit the style of the house and had it ready on time for the first open house. Her blend of real estate and design made her a perfect partner.<span class="quote__by">Grace H.</span></p>
    <p class="quote">The marketing and staging of our house was on point. I don’t think the sale would have gone as smoothly without her.<span class="quote__by">Sam &amp; Jo W.</span></p>
    <p class="quote">I have had several real estate dealings with Marta and each one was handled professionally and with my best interest in mind. Her marketing skills are top notch; she made sure my homes were ready for market and showcased them in the best way through staging and professional photography. She kept the sales on track and I keep recommending her to family and friends.<span class="quote__by">Nora B.</span></p>
    <p class="quote">Marta worked with our builder to help design new floor plans and chose the selections and finishes, then staged and decorated the model homes using furniture from old models and some new pieces. The feedback was amazing and the homes sold quickly. She was responsive with updates and reports, and we will use her again.<span class="quote__by">Owen F.</span></p>
  </div>

  <div class="photo" role="img" aria-label="Portrait of the broker standing in a staged living room with fireplace and white sofa" style="left:262px;top:105px;width:538px;height:299px;background:linear-gradient(100deg,#e9e4dc 0%,#cfc5b6 35%,#8d7a64 55%,#d8d2c9 75%,#3b3a3c 100%)"></div>

  <div class="abs headline-box">PROVEN MARKET<br>KNOWLEDGE</div>

  <div class="abs contact-panel">
    <div class="brand brand--navy">
      <div class="brand__name">BRAVE</div>
      <div class="brand__sub">REALTY LLC</div>
    </div>
    <ul class="contact-list">
      <li><svg class="icon" viewBox="0 0 12 12"><circle cx="6" cy="6" r="6" fill="#1f2d5c"/><path d="M4 3h1.3l.6 1.6-.8.6a4 4 0 0 0 1.7 1.7l.6-.8 1.6.6V8.3A.8.8 0 0 1 8.3 9 5.5 5.5 0 0 1 3 3.7.8.8 0 0 1 4 3z" fill="#fff"/></svg>860-912-7048</li>
      <li><svg class="icon" viewBox="0 0 12 12"><circle cx="6" cy="6" r="6" fill="#1f2d5c"/><rect x="3" y="4" width="6" height="4.2" fill="none" stroke="#fff" stroke-width=".9"/><path d="M3 4l3 2.3L9 4" fill="none" stroke="#fff" stroke-width=".9"/></svg>Marta@LOMAVERTPA.com</li>
      <li><svg class="icon" viewBox="0 0 12 12"><circle cx="6" cy="6" r="6" fill="#1f2d5c"/><circle cx="6" cy="6" r="3.3" fill="none" stroke="#fff" stroke-width=".8"/><path d="M2.7 6h6.6M6 2.7c-1.6 2-1.6 4.6 0 6.6M6 2.7c1.6 2 1.6 4.6 0 6.6" fill="none" stroke="#fff" stroke-width=".7"/></svg>www.lomavertpa.com</li>
    </ul>
  </div>

  <div class="abs agent">
    <p class="agent__name">Marta Venholt</p>
    <p class="agent__role">Owner Broker</p>
    <p class="agent__role">Stager Re-Designer</p>
    <ul class="agent__contacts">
      <li>860-912-7048<svg class="icon" viewBox="0 0 12 12"><circle cx="6" cy="6" r="5.4" fill="none" stroke="#1f2d5c"/><path d="M4 3h1.3l.6 1.6-.8.6a4 4 0 0 0 1.7 1.7l.6-.8 1.6.6V8.3A.8.8 0 0 1 8.3 9 5.5 5.5 0 0 1 3 3.7.8.8 0 0 1 4 3z" fill="#1f2d5c"/></svg></li>
      <li>Marta@LOMAVERTPA.com<svg class="icon" viewBox="0 0 12 12"><circle cx="6" cy="6" r="5.4" fill="none" stroke="#1f2d5c"/><rect x="3.2" y="4.2" width="5.6" height="3.8" fill="none" stroke="#1f2d5c" stroke-width=".8"/><path d="M3.2 4.2L6 6.3l2.8-2.1" fill="none" stroke="#1f2d5c" stroke-width=".8"/></svg></li>
      <li>www.lomavertpa.com<svg class="icon" viewBox="0 0 12 12"><circle cx="6" cy="6" r="5.4" fill="none" stroke="#1f2d5c"/><circle cx="6" cy="6" r="3" fill="none" stroke="#1f2d5c" stroke-width=".7"/><path d="M3 6h6M6 3c-1.4 1.8-1.4 4.2 0 6M6 3c1.4 1.8 1.4 4.2 0 6" fill="none" stroke="#1f2d5c" stroke-width=".6"/></svg></li>
    </ul>
  </div>

  <div class="abs band-bottom" style="left:0;width:800px"></div>
  <div class="fold fold--a" style="left:262px"></div>
  <div class="fold fold--b" style="left:511px"></div>
</section>

<section class="spread spread--inside">
  <div class="abs intro">
    <div class="brand brand--navy">
      <div class="brand__name">BRAVE</div>
      <div class="brand__sub">REALTY LLC</div>
    </div>
    <div class="intro__text">
      <p>Selling Real Estate has changed drastically in the last few years. Today’s real estate processes are multi-faceted undertakings that encompass significant emotional and financial components. Having the right marketing partner is so important; one who works to protect your best interests while capably navigating you through the many complexities of the real estate transaction is vital.</p>
      <p>Marta Venholt Real Estate Marketing Specialist truly understands not only the legal process needed but also recognizes buyer trends and knows how to “showcase” a property to sell targeted to the proper consumer demographic. A home is one of your most valuable assets. If you are thinking about selling a property, it is crucial that you hire someone with an extraordinary history of happy sellers.</p>
    </div>
  </div>
  <div class="photo" role="img" aria-label="Kitchen photograph blending into a line sketch, framed by two hands" style="left:0;top:372px;width:265px;height:248px;background:linear-gradient(90deg,#c9b49a 0%,#e7e1d8 45%,#f4f4f4 100%)"></div>

  <div class="photo" role="img" aria-label="Staged living room with rustic table, armchairs and fireplace" style="left:265px;top:0;width:535px;height:135px;background:linear-gradient(180deg,#b7aa9a 0%,#8a7661 55%,#6a5847 100%)"></div>

  <div class="abs staging">
    <div class="thumb" role="img" aria-label="Empty room before staging" style="left:13px;top:10px;background:linear-gradient(160deg,#d8d3cc,#6b5a49)"><span class="thumb__label">BEFORE</span></div>
    <div class="thumb" role="img" aria-label="Dining room after staging" style="left:140px;top:10px;background:linear-gradient(160deg,#d9d6d2,#5e4a3a)"><span class="thumb__label">AFTER</span></div>
    <div class="thumb" role="img" aria-label="Empty bedroom before staging" style="left:278px;top:10px;background:linear-gradient(160deg,#cfcfcd,#5a4535)"><span class="thumb__label">BEFORE</span></div>
    <div class="thumb" role="img" aria-label="Bedroom after staging" style="left:405px;top:10px;background:linear-gradient(160deg,#ebe6e2,#8b7766)"><span class="thumb__label">AFTER</span></div>
    <div class="thumb" role="img" aria-label="Bedroom before staging" style="left:13px;top:95px;background:linear-gradient(160deg,#b8b9bb,#4f4540)"><span class="thumb__label">BEFORE</span></div>
    <div class="thumb" role="img" aria-label="Bedroom after staging" style="left:140px;top:95px;background:linear-gradient(160deg,#d1cbc3,#5a4536)"><span class="thumb__label">AFTER</span></div>
    <div class="thumb" role="img" aria-label="Kitchen before staging" style="left:278px;top:95px;background:linear-gradient(160deg,#c5b9a8,#5c3f29)"><span class="thumb__label">BEFORE</span></div>
    <div class="thumb" role="img" aria-label="Kitchen after staging" style="left:405px;top:95px;background:linear-gradient(160deg,#f1efeb,#9d7f63)"><span class="thumb__label">AFTER</span></div>
  </div>

  <div class="abs copy" style="left:280px;width:237px">
    <p>Marta devotes her efforts to selling real estate, by keeping up with the evolving market, researching buyer trends and preparing homes before they enter the market by staging them to connect with the target buyer.</p>
    <p>Marta knows all sales are not alike. Therefore, taking a cookie cutter approach is not acceptable, she recognizes that each property is unique and requires a personalized marketing plan and strategy.</p>
    <p>A veteran in the real estate industry with nearly 30 years expertise and consistent membership in the Multi-Million-Dollar Club combined with her Valera Home Stager and Re-Designer credentials assures that her clients get the advantage of vast</p>
  </div>
  <div class="abs copy" style="left:547px;width:235px">
    <p>knowledge, seasoned experience and proven results, all geared to creating beautiful spaces, which form a connection with the right buyer producing the <strong>highest and best offer.</strong></p>
    <h3>Proven Market Knowledge</h3>
    <p>That’s what you can expect when you work with seasoned specialist Marta Venholt for all your Real Estate needs.</p>
    <p>The sale of a home is too important an undertaking to entrust to just anyone. Select a dedicated, service-oriented and results-driven broker who understands the intricacies of the Real Estate process...select Marta.</p>
  </div>
  <div class="abs site-button">www.lomavertpa.com</div>

  <div class="abs band-bottom" style="left:265px;width:535px"></div>
  <div class="fold fold--a" style="left:265px"></div>
  <div class="fold fold--b" style="left:519px"></div>
</section>

</body>
</html>
```